Strategic Objective - Internal

Take text supplied in a word document and make a stylish, professional document using elements of our brand .This is an internal document for presentation to our small team . Have attached an example document - please do not copy this - this is just to give you the concept. I would like to be able to edit the text in the document you supply back to me also (In word or photoshop)

Our website is www.harrowvt.com.au

Have attached out logo
Thank you

Target Market(s)

Our staff

Industry/Entity Type

Mining, Earthmoving

Requirements
Must have
• Professional, stylish presentation
Nice to have
• Our market includes Australia, Papua New Guinea and teh South Pacific - any graphic that supports this. We are an importer and exporter - any graphics that support this.

```html
<!DOCTYPE html>
<html lang="en">
<head>
<meta charset="utf-8">
<title>Harrow VT – 2024-2025 Financial Year</title>
<link href="https://fonts.googleapis.com/css2?family=Oswald:wght@400;500;600&family=Encode+Sans+Condensed:wght@400;700&display=swap" rel="stylesheet">
<style>
:root{
  --backdrop:#e0e0e0;
  --paper:#ffffff;
  --ink:#1c1c1c;
  --text:#2a2a2a;
  --yellow:#f4b400;
  --cream:#fdf1d2;
  --rule:#9a9a9a;
  --brand:#3b2f8f;
  --green:#7dbb2f;
  --photo-a:#6b5a3a;
  --photo-b:#e0a21a;
}
*{box-sizing:border-box;margin:0;padding:0}
html,body{width:1200px;height:3035px;overflow:hidden;background:var(--backdrop)}
.sheet{position:relative;width:1018px;height:2576px;transform:scale(1.17878);transform-origin:0 0}
.page{position:absolute;background:var(--paper);width:373px;height:527px;overflow:hidden;box-shadow:0 14px 18px -10px rgba(0,0,0,.35);font-family:"Encode Sans Condensed",sans-serif;color:var(--text)}
.abs{position:absolute}
.wordmark{position:absolute;display:flex;align-items:center;gap:4px;font-family:"Oswald",sans-serif;font-weight:600;letter-spacing:.5px;white-space:nowrap}
.wordmark .dot{width:9px;height:9px;border-radius:50%;background:var(--green)}
.header .wordmark{left:14px;top:18px;font-size:12px;color:#fff}
.section-head{position:absolute;left:57px;width:281px;display:flex;align-items:flex-end;gap:4px;font-family:"Oswald",sans-serif;font-weight:500;font-size:11px;color:var(--ink);text-transform:uppercase}
.section-head svg{flex:none;margin-bottom:1px}
.section-head .line{flex:1;border-bottom:1px solid var(--rule);margin-bottom:2px}
.col{position:absolute;width:116px;font-size:6.4px;line-height:10px;text-align:justify}
.col b{font-weight:700;color:var(--ink)}
.col p+p{margin-top:10px}
.tangibles{position:absolute;left:222px;top:162px;width:116px;font-size:6.4px;border-collapse:separate;border-spacing:0 1px}
.tangibles td{height:10px;padding:0 3px;font-weight:700;color:var(--ink)}
.tangibles tr.shade td{background:var(--cream)}
.folio{position:absolute;left:28px;width:30px;text-align:center;font-family:"Oswald",sans-serif;color:var(--ink)}
.folio .num{font-size:11px;font-weight:500;line-height:12px;border-bottom:1px solid var(--rule);padding-bottom:1px}
.folio .yr{font-size:5.5px;font-weight:600;line-height:7px;margin-top:2px}
.folio .fy{font-size:4.5px;line-height:5px}
.foot-bar{position:absolute;left:92px;top:512px;width:279px;height:12px;background:var(--ink)}
.photo{position:absolute}
.closing{position:absolute;left:0;width:100%;text-align:center;font-family:"Oswald",sans-serif;color:var(--ink)}
.closing .wordmark{position:static;justify-content:center;color:var(--brand);font-size:14px}
</style>
</head>
<body>
<div class="sheet">

  <!-- Cover spread: back cover -->
  <div class="page back-cover" style="left:130px;top:60px">
    <div class="photo" role="img" aria-label="Photo of a yellow mining haul truck" style="left:120px;top:180px;width:140px;height:80px;border-radius:6px;background:linear-gradient(160deg,#e8b21e,#8a6a20)"></div>
    <div class="closing" style="top:272px">
      <div class="wordmark"><span class="dot"></span>HARROW VT</div>
      <div style="font-size:15px;margin-top:2px">2024-2025</div>
      <div style="font-size:11px;line-height:12px">Financial Year</div>
    </div>
  </div>

  <!-- Cover spread: front cover -->
  <div class="page front-cover" style="left:509px;top:60px">
    <div class="photo" role="img" aria-label="Faint line drawing of a wheel loader" style="left:95px;top:60px;width:270px;height:240px;background:linear-gradient(180deg,#f6f6f6,#ececec)"></div>
    <div class="wordmark" style="right:24px;top:40px;font-size:20px;color:var(--brand)"><span class="dot" style="width:14px;height:14px"></span>HARROW VT</div>
    <svg class="abs" style="left:0;top:0" width="379" height="527" viewBox="0 0 373 527">
      <polygon points="0,300 373,215 373,240 0,325" fill="var(--yellow)"/>
      <polygon points="0,325 373,240 373,527 0,527" fill="var(--ink)"/>
      <polygon points="110,345 373,290 373,318 110,373" fill="var(--yellow)"/>
      <g fill="var(--ink)">
        <polygon points="150,362 160,340 168,338 158,360"/>
        <polygon points="176,356 186,334 194,332 184,354"/>
        <polygon points="202,351 212,329 220,327 210,349"/>
        <polygon points="228,345 238,323 246,321 236,343"/>
      </g>
    </svg>
    <div class="photo" role="img" aria-label="Photo of a yellow wheel loader with raised bucket" style="left:140px;top:205px;width:200px;height:110px;border-radius:8px;background:linear-gradient(150deg,#3a3a3a 0%,#3a3a3a 35%,var(--photo-b) 36%,#b57d10 100%)"></div>
    <div class="abs" style="left:150px;top:385px;font-family:'Oswald',sans-serif;font-weight:600;font-size:38px;line-height:40px;color:var(--yellow)">2024-2025</div>
    <div class="abs" style="left:250px;top:428px;font-family:'Oswald',sans-serif;font-size:11px;color:#fff">Financial Year</div>
  </div>

  <!-- Page 2 -->
  <div class="page inner" style="left:310px;top:643px">
    <svg class="abs header-art" style="left:0;top:0" width="373" height="66" viewBox="0 0 373 66">
      <defs><linearGradient id="ph2" x1="0" y1="0" x2="1" y2="1"><stop offset="0" stop-color="#4a3a22"/><stop offset=".6" stop-color="var(--photo-b)"/><stop offset="1" stop-color="#5a4a30"/></linearGradient></defs>
      <polygon points="0,0 125,0 108,50 0,50" fill="var(--ink)"/>
      <polygon points="125,0 140,0 123,50 108,50" fill="var(--yellow)"/>
      <polygon points="140,0 373,0 373,50 123,50" fill="url(#ph2)" role="img" aria-label="Photo of an underground loader"/>
      <rect x="0" y="50" width="373" height="2" fill="var(--rule)"/>
      <polygon points="0,53 118,53 114,66 0,66" fill="var(--yellow)"/>
      <g fill="var(--ink)"><polygon points="55,66 59,53 68,53 64,66"/><polygon points="70,66 74,53 83,53 79,66"/><polygon points="85,66 89,53 98,53 94,66"/><polygon points="100,66 104,53 113,53 109,66"/></g>
    </svg>
    <div class="header"><div class="wordmark"><span class="dot"></span>HARROW VT</div></div>

    <div class="section-head" style="top:131px"><svg width="32" height="9"><g fill="var(--yellow)"><polygon points="0,9 4,0 10,0 6,9"/><polygon points="11,9 15,0 21,0 17,9"/><polygon points="22,9 26,0 32,0 28,9"/></g></svg><span>Tangibles</span><span class="line"></span></div>
    <div class="col" style="left:92px;top:162px;text-align:left">In the 2024-2025 Financial year we will have</div>
    <table class="tangibles">
      <tr class="shade"><td>Annual turnover of</td><td>18M</td></tr>
      <tr><td></td><td>21% GP</td></tr>
      <tr class="shade"><td>Average Quotes per week</td><td>200</td></tr>
      <tr><td>Conversion rate</td><td>52%</td></tr>
      <tr class="shade"><td>Annual growth rate of</td><td>10%</td></tr>
    </table>

    <div class="section-head" style="top:235px"><svg width="32" height="9"><g fill="var(--yellow)"><polygon points="0,9 4,0 10,0 6,9"/><polygon points="11,9 15,0 21,0 17,9"/><polygon points="22,9 26,0 32,0 28,9"/></g></svg><span>Our Brand Promise</span><span class="line"></span></div>
    <div class="col" style="left:92px;top:266px">In every interaction with our business our customers know that they are working with the best – they will not find better service or overall value anywhere else – and this gets reinforced by every interaction they have with us. As well as the physical products they are buying peace of mind.</div>
    <div class="col" style="left:222px;top:266px;text-align:left">We define being the best in terms of Knowledge, Responsiveness, Accuracy, Competitive pricing, Consistency and Understanding</div>

    <div class="section-head" style="top:362px"><svg width="32" height="9"><g fill="var(--yellow)"><polygon points="0,9 4,0 10,0 6,9"/><polygon points="11,9 15,0 21,0 17,9"/><polygon points="22,9 26,0 32,0 28,9"/></g></svg><span>Our Core Values</span><span class="line"></span></div>
    <div class="col" style="left:92px;top:393px"><p><b>Commitment to Excellence</b> - we turn up every day ready to be the best person we can be and deliver the best possible outcome and experience for our customer. Set a high bar and always seek to improve.</p><p><b>Accuracy</b> - how we do the little things is how we do everything. Detail matters. We never assume… we make certain</p></div>
    <div class="col" style="left:222px;top:393px"><b>Growth</b> – our knowledge, Experience, and Skills. Personal &amp; professional. Be curious and interested.<br>Respect – Listen first and understand. Everyone is valued.</div>

    <div class="folio" style="top:471px"><div class="num">2</div><div class="yr">2024-2025</div><div class="fy">Financial Year</div></div>
    <div class="foot-bar"></div>
  </div>

  <!-- Page 3 -->
  <div class="page inner" style="left:310px;top:1246px">
    <svg class="abs header-art" style="left:0;top:0" width="373" height="66" viewBox="0 0 373 66">
      <defs><linearGradient id="ph3" x1="0" y1="0" x2="0" y2="1"><stop offset="0" stop-color="#b9b6b0"/><stop offset=".45" stop-color="#e09a2a"/><stop offset="1" stop-color="#9a6a40"/></linearGradient></defs>
      <polygon points="0,0 125,0 108,50 0,50" fill="var(--ink)"/>
      <polygon points="125,0 140,0 123,50 108,50" fill="var(--yellow)"/>
      <polygon points="140,0 373,0 373,50 123,50" fill="url(#ph3)" role="img" aria-label="Photo of an articulated dump truck on site"/>
      <rect x="0" y="50" width="373" height="2" fill="var(--rule)"/>
      <polygon points="0,53 118,53 114,66 0,66" fill="var(--yellow)"/>
      <g fill="var(--ink)"><polygon points="55,66 59,53 68,53 64,66"/><polygon points="70,66 74,53 83,53 79,66"/><polygon points="85,66 89,53 98,53 94,66"/><polygon points="100,66 104,53 113,53 109,66"/></g>
    </svg>
    <div class="header"><div class="wordmark"><span class="dot"></span>HARROW VT</div></div>

    <div class="section-head" style="top:131px"><svg width="32" height="9"><g fill="var(--yellow)"><polygon points="0,9 4,0 10,0 6,9"/><polygon points="11,9 15,0 21,0 17,9"/><polygon points="22,9 26,0 32,0 28,9"/></g></svg><span>Culture</span><span class="line"></span></div>
    <div class="col" style="left:92px;top:162px">We pride ourselves on a collaborative and harmonious work environment where we support each other respectfully. Every team member feels seen, heard, and understood. Team members must love the company before the clients can love the company. Our team members truly want to work here… not because of the paycheck but because they feel valued, enjoy what they do and are making a difference to our clients' businesses and lives.</div>
    <div class="col" style="left:222px;top:162px">Our Team members are confident enough to have hard conversations while always assuming the best intentions of their fellow team member. Team members hold each other accountable for what they are supposed to be doing because it is the right thing to do. Team members can honestly tell their family and friends that they love working for our company. Team members give more effort than expected because they want to, not because they must, or for a reward. All team members feel seen, heard, and understood.</div>

    <div class="section-head" style="top:301px"><svg width="32" height="9"><g fill="var(--yellow)"><polygon points="0,9 4,0 10,0 6,9"/><polygon points="11,9 15,0 21,0 17,9"/><polygon points="22,9 26,0 32,0 28,9"/></g></svg><span>At Harrow VT we are committed to….</span><span class="line"></span></div>
    <div class="col" style="left:92px;top:332px;text-align:left">Compensating team members well.<br>Making the highest priority our team members': health, family, and growth. These three all come before work.<br>Providing coaching and other forms of self-improvement.<br>Having a friendly and welcoming environment.<br>Having clarity around roles and responsibilities including regular mentoring<br>Hiring and retaining the right team members that align with our values</div>
    <div class="col" style="left:222px;top:332px"><p>Our goal is for team members to say: "I love working here" I enjoy working with our clients and suppliers and I know we are making a difference. I enjoy doing meaningful work. I am paid well for the work I am doing. I enjoy working with my colleagues and talking to them about what is happening in their personal and professional life. We have a great work environment. We work hard and have fun together.</p><p>Everyone who works here contributes to creating the culture we want.</p></div>

    <div class="folio" style="top:472px"><div class="num">3</div><div class="yr">2024-2025</div><div class="fy">Financial Year</div></div>
    <div class="foot-bar" style="left:94px;width:277px"></div>
  </div>

  <!-- Back page -->
  <div class="page back-page" style="left:308px;top:1868px;width:374px;height:530px">
    <div class="photo" role="img" aria-label="Photo of a yellow mining haul truck" style="left:114px;top:267px;width:163px;height:90px;border-radius:6px;background:linear-gradient(160deg,#e8b21e,#8a6a20)"></div>
    <div class="closing" style="top:374px">
      <div class="wordmark"><span class="dot"></span>HARROW VT</div>
      <div style="font-size:15px;margin-top:2px">2024-2025</div>
      <div style="font-size:11px;line-height:12px">Financial Year</div>
    </div>
  </div>

</div>
</body>
</html>
```